Business Card Design Project

Financial planning, Insurance and Real estate - Financial Services company

Contact Information for Business Card

Looking for something simple in design -
Brindlewood Capital LLC
Brindlewood Wealth Managment

```html
<!DOCTYPE html>
<html lang="en">
<head>
<meta charset="utf-8">
<title>Brindlewood Wealth Management – Business Card</title>
<link href="https://fonts.googleapis.com/css2?family=Open+Sans:wght@400;600;700&display=swap" rel="stylesheet">
<style>
  :root {
    --backdrop: #2a2a2a;
    --card: #1c1c1d;
    --card-edge: #262627;
    --ink-white: #f2f2f2;
    --ink-grey: #c9c9c9;
    --rule: #5a5a5a;
    --brand-blue: #1a86c8;
  }
  * { margin: 0; padding: 0; box-sizing: border-box; }
  html, body {
    width: 1200px; height: 900px; overflow: hidden;
    background: var(--backdrop);
    font-family: "Open Sans", Arial, sans-serif;
  }
  .stage { position: relative; width: 1200px; height: 900px; }
  .card {
    position: absolute;
    width: 620px; height: 354px;
    background: var(--card);
    border: 1px solid var(--card-edge);
    border-radius: 24px;
    box-shadow: 0 18px 40px rgba(0,0,0,.45);
  }

  /* Back of card */
  .card-back { left: 110px; top: 80px; }
  .card-back .brand-mark {
    position: absolute; left: 0; right: 0; top: 110px;
    display: flex; align-items: center; justify-content: center; gap: 14px;
  }
  .brand-dot {
    width: 22px; height: 22px; border-radius: 50%;
    border: 3px solid currentColor;
  }
  .card-back .brand-mark { color: var(--ink-white); }
  .brand-name { font-weight: 700; font-size: 24px; letter-spacing: .5px; }
  .card-back .rule {
    position: absolute; left: 150px; right: 150px; top: 254px;
    height: 1px; background: var(--rule);
  }
  .website {
    position: absolute; left: 0; right: 0; top: 270px;
    text-align: center; color: var(--ink-white);
    font-size: 15px; letter-spacing: 5px;
  }

  /* Front of card */
  .card-front { left: 470px; top: 470px; }
  .card-front .brand-mark {
    position: absolute; right: 34px; top: 48px;
    display: flex; align-items: center; gap: 10px;
    color: var(--brand-blue);
  }
  .card-front .brand-name { font-size: 17px; letter-spacing: 0; }
  .card-front .brand-dot { width: 18px; height: 18px; }
  .divider {
    position: absolute; left: 34px; right: 34px; top: 112px;
    height: 1px; background: var(--rule);
  }
  .services {
    position: absolute; right: 34px; top: 128px;
    list-style: none; text-align: right;
    color: var(--ink-grey); font-size: 15px; line-height: 22px;
  }
  .services li::after {
    content: ""; display: inline-block; width: 7px; height: 7px;
    margin-left: 9px; vertical-align: middle;
    border-radius: 50%; background: var(--brand-blue);
  }
  .person-name {
    position: absolute; left: 34px; top: 220px;
    color: var(--brand-blue); font-weight: 700; font-size: 20px;
  }
  .person-rule {
    position: absolute; left: 34px; width: 230px; top: 252px;
    height: 1px; background: var(--rule);
  }
  .contacts {
    position: absolute; left: 34px; top: 262px;
    list-style: none; color: var(--ink-grey);
    font-size: 15px; line-height: 22px;
  }
  .contacts li { display: flex; align-items: center; gap: 9px; }
  .contacts svg { width: 14px; height: 14px; fill: var(--brand-blue); flex: none; }
</style>
</head>
<body>
<main class="stage">

  <section class="card card-back" aria-label="Card back">
    <div class="brand-mark">
      <span class="brand-dot"></span>
      <span class="brand-name">Brindlewood Wealth Management</span>
    </div>
    <div class="rule"></div>
    <p class="website">www.brindlewoodwm.com</p>
  </section>

  <section class="card card-front" aria-label="Card front">
    <div class="brand-mark">
      <span class="brand-dot"></span>
      <span class="brand-name">Brindlewood Wealth Management</span>
    </div>
    <div class="divider"></div>
    <ul class="services">
      <li>Financial Planning</li>
      <li>Insurance</li>
      <li>Real Estate</li>
    </ul>

    <h1 class="person-name">Daniel Harper</h1>
    <div class="person-rule"></div>
    <ul class="contacts">
      <li>
        <svg viewBox="0 0 14 14" aria-hidden="true"><path d="M4 0h6a1 1 0 0 1 1 1v12a1 1 0 0 1-1 1H4a1 1 0 0 1-1-1V1a1 1 0 0 1 1-1zm0 2v9h6V2zm3 9.6a.8.8 0 1 0 0 1.6.8.8 0 0 0 0-1.6z"/></svg>
        425-555-0143
      </li>
      <li>
        <svg viewBox="0 0 14 14" aria-hidden="true"><path d="M3 0h8v4H3zM1 5h12a1 1 0 0 1 1 1v5h-3v3H3v-3H0V6a1 1 0 0 1 1-1zm3 5v3h6v-3z"/></svg>
        425-555-0187
      </li>
      <li>
        <svg viewBox="0 0 14 14" aria-hidden="true"><path d="M0 3h14v1L7 8 0 4zm0 2.3 7 4 7-4V12H0z"/></svg>
        daniel@brindlewoodwm.com
      </li>
    </ul>
  </section>

</main>
</body>
</html>
```